Powerpoint Sales and Pre-Sales Decks

We need a GD to support us as we start buillidng many PPT decks - we are a start-up based in London in the Telecomms space

```html
<!DOCTYPE html>
<html lang="en">
<head>
<meta charset="utf-8">
<title>Relay Pitch – Sales Deck Template</title>
<link href="https://fonts.googleapis.com/css2?family=Lato:wght@300;400;700&display=swap" rel="stylesheet">
<style>
:root{
  --navy:#2d3541;
  --slate:#434d5c;
  --green:#6cc29a;
  --blue:#4a8cc2;
  --orange:#e8843a;
  --red:#d9473f;
  --lime:#8fbf3c;
  --olive:#7e9a3a;
  --ink:#2d3541;
  --grey:#8a8f96;
  --line:#e3e5e8;
  --page:#ffffff;
}
*{box-sizing:border-box;margin:0;padding:0}
html,body{width:1200px;height:4435px;overflow:hidden;background:var(--page)}
body{font-family:"Lato",sans-serif;color:var(--ink)}
.deck{width:1200px;height:4435px;padding:31px 21px 0;display:grid;grid-template-columns:566px 566px;column-gap:24px;row-gap:21px;grid-auto-rows:318px}
.slide{position:relative;background:#fff;overflow:hidden;box-shadow:0 2px 7px rgba(0,0,0,.16)}
.slide.dark{background:var(--navy);color:#fff}
.num{position:absolute;top:9px;right:9px;width:12px;height:12px;background:#d5d8dc;color:#fff;font-size:6px;line-height:12px;text-align:center;border-radius:2px;z-index:3}
.dark .num{background:#4a5464}
.ttl{font-size:15px;font-weight:400;text-align:center;color:var(--ink);padding-top:26px}
.dark .ttl{color:#fff}
.sub{font-size:6.5px;color:var(--green);text-align:center;margin-top:4px}
.tx{font-size:6px;line-height:1.65;color:var(--grey)}
.dark .tx{color:#c9ced6}
.c{text-align:center}
.ph{background:linear-gradient(135deg,#8a8f96,#4d545e)}
.ph.warm{background:linear-gradient(135deg,#c9a98e,#6e5a4c)}
.ph.cool{background:linear-gradient(135deg,#9aa7b4,#3d4754)}
.ph.light{background:linear-gradient(135deg,#dcdcd8,#9a9c9e)}
.ph.dusk{background:linear-gradient(135deg,#d1b07a,#5b5a58)}
.stripes{position:absolute;inset:0;width:100%;height:100%}
.soc{display:flex;gap:8px;justify-content:center;margin-top:6px}
.soc i{display:block;width:7px;height:7px;background:var(--green);border-radius:1.5px}
.name{font-size:7px;font-weight:700;color:var(--ink);margin-top:6px}
.role{font-size:5.5px;color:var(--green);margin-top:2px}
.cover{position:absolute;left:0;right:0;top:70px;text-align:center}
.brand{display:inline-flex;flex-direction:column;align-items:center;gap:8px;font-size:15px;font-weight:400}
.brand b{display:block;width:30px;height:30px;background:#fff}
.cover .sub{margin-top:5px}
.cover .tx{width:300px;margin:6px auto 0}
.band{position:absolute;left:0;right:0;top:104px;height:135px;display:grid;grid-template-columns:180px 1fr 180px}
.band .mid{background:var(--navy);color:#fff;text-align:center;padding:14px 26px 0}
.ico{width:14px;height:14px;border-radius:50%;background:#fff;margin:0 auto}
.band h3{font-size:9px;font-weight:400;margin-top:8px}
.avatar{width:76px;height:76px;border-radius:50%;margin:56px auto 0;border:2px solid #fff;box-shadow:0 0 0 1px var(--line)}
.rule{width:70px;height:1px;background:var(--blue);margin:6px auto}
.para{width:400px;margin:10px auto 0;text-align:center}
.sq-ico{width:26px;height:26px;background:var(--navy);border-radius:3px;margin:72px auto 0;position:relative}
.sq-ico::after{content:"";position:absolute;left:8px;top:8px;width:10px;height:10px;background:#fff;border-radius:1px}
.half{position:absolute;left:0;right:0;top:0;height:190px;background:var(--navy);text-align:center;color:#fff}
.pin{width:7px;height:9px;margin:5px auto 0;border:1.5px solid #fff;border-radius:50% 50% 50% 0;transform:rotate(-45deg)}
.list{display:grid;grid-template-columns:1fr 1fr;column-gap:30px;row-gap:14px;padding:16px 36px 0}
.item{display:flex;gap:12px}
.item h4{font-size:6px;font-weight:400;color:var(--ink);margin-bottom:2px}
.dot{flex:none;width:24px;height:24px;border-radius:50%;position:relative}
.dot::after{content:"";position:absolute;left:8px;top:8px;width:8px;height:8px;border-radius:50%;background:#fff}
.n{flex:none;width:24px;font-size:16px;font-weight:300;line-height:1}
.nb{flex:none;width:24px;height:24px;color:#fff;font-size:12px;font-weight:300;display:flex;align-items:center;justify-content:center}
.section{position:absolute;left:36px;top:110px;width:300px}
.section .sym{width:22px;height:18px;border:2px solid #fff;border-radius:2px;margin-bottom:10px}
.section h2{font-size:14px;font-weight:400}
.section .sub{text-align:left;margin:3px 0 5px}
.team{display:grid;gap:6px;padding:14px 36px 0}
.team .tx{font-size:5px;text-align:center}
.success{position:absolute;left:0;right:0;top:62px;height:140px;background:var(--green);display:grid;grid-template-columns:200px 1fr}
.success .ph{margin:-30px 30px 0 60px;background:linear-gradient(135deg,#7b8591,#30363f)}
.success .body{padding:50px 34px 0 0;color:#fff}
.success h4{font-size:7px;font-weight:400;margin-bottom:3px}
.success .tx{color:#eefaf4}
.six{display:grid;grid-template-columns:1fr 1fr;column-gap:30px;row-gap:12px;padding:14px 36px 0}
.six .card{display:flex;gap:10px}
.six .ph{width:44px;height:50px;flex:none}
.six .soc{justify-content:flex-start;margin-top:3px}
.tiles{display:grid;grid-template-columns:repeat(6,1fr);grid-template-rows:95px 95px}
.tile{color:#fff;font-size:5px;line-height:1.5;padding:14px 10px;text-align:center}
.tile i{display:block;width:8px;height:8px;background:#fff;border-radius:50%;margin:0 auto 6px}
.itd{position:absolute;left:0;right:0;top:74px;height:170px;display:grid;grid-template-columns:210px 1fr}
.itd .panel{background:var(--slate);padding:30px 30px 0}
.itd h4,.twin h4{font-size:7px;font-weight:400;color:#fff;margin-bottom:4px}
.circles{display:flex;gap:12px;margin-top:16px}
.circles i{width:24px;height:24px;border-radius:50%;display:block;position:relative}
.circles i::after{content:"";position:absolute;left:8px;top:8px;width:8px;height:8px;background:#fff;border-radius:50%}
.foot{position:absolute;left:36px;right:36px;bottom:22px;text-align:center}
.intro{padding:14px 36px 0}
.gal{display:grid;gap:10px;padding:12px 36px 0}
.gal h5{font-size:5.5px;font-weight:700;color:var(--ink);margin:6px 0 2px}
.gal .tx{font-size:5px}
.twin{position:absolute;left:0;right:0;top:74px;height:170px;display:grid;grid-template-columns:190px 1fr 190px}
.twin .panel{background:var(--green);padding:26px 22px 0;text-align:center}
.twin .tx{color:#f1fbf6}
.twin .circles{justify-content:center}
.ti{position:absolute;left:36px;right:36px;top:72px;height:220px;display:grid;grid-template-columns:95px 1fr;grid-template-rows:1fr 1fr}
.ti .txt{padding:16px 20px 0}
.ti h5{font-size:7px;font-weight:400;color:#fff;margin-bottom:4px;opacity:.9}
.tl{position:absolute;inset:4px;display:grid;grid-template-columns:repeat(6,1fr);grid-template-rows:repeat(4,1fr);gap:4px}
.tl>div{color:#fff;font-size:5px;line-height:1.5;padding:8px;overflow:hidden}
.tl .yr{font-size:11px;font-weight:300;display:block;margin-bottom:4px}
.tl .vert{display:flex;align-items:center;justify-content:center;font-size:11px;font-weight:300;padding:0}
.tl .vert span{transform:rotate(-90deg);white-space:nowrap}
</style>
</head>
<body>
<main class="deck">

<section class="slide dark">
  <span class="num">1</span>
  <div class="cover">
    <div class="brand"><b></b>Relay Pitch</div>
    <p class="sub">Ultimate Presentation Template</p>
    <p class="tx">Fast links for busy teams. We plan, test and run each line so your calls stay clear.</p>
  </div>
  <svg class="stripes" viewBox="0 0 566 318" aria-hidden="true">
    <polygon points="455,318 467,318 566,202 566,188" fill="var(--blue)"/>
    <polygon points="470,318 515,318 566,258 566,205" fill="var(--green)"/>
  </svg>
</section>

<section class="slide">
  <span class="num">2</span>
  <h2 class="ttl">Welcome</h2>
  <p class="sub">Put your Subtitle in this place</p>
  <div class="band">
    <div class="ph cool" role="img" aria-label="Photo of an empty meeting room"></div>
    <div class="mid">
      <div class="ico"></div>
      <h3>Welcome to this project</h3>
      <p class="sub">Subtitle for this project</p>
      <p class="tx" style="margin-top:5px">Fast links for busy teams. We plan, test and run each line so your calls stay clear.</p>
    </div>
    <div class="ph light" role="img" aria-label="Photo of a notebook and pen on a desk"></div>
  </div>
</section>

<section class="slide">
  <span class="num">3</span>
  <div class="avatar ph warm" style="margin-top:56px" role="img" aria-label="Portrait photo of the chief executive"></div>
  <p class="name c" style="font-weight:400;font-size:8px">Clara Vance</p>
  <p class="sub">CEO &amp; President</p>
  <div class="rule"></div>
  <p class="tx para">Our team plans and runs fast fibre and mobile links for firms across the city. We test each line, watch every node and fix faults before clients notice, so teams stay online and calls stay clear all day long.</p>
</section>

<section class="slide">
  <span class="num">4</span>
  <div class="sq-ico"></div>
  <p class="name c" style="font-weight:400;font-size:8px;margin-top:10px">Introduction</p>
  <p class="sub">Put your Subtitle in this place</p>
  <div class="rule"></div>
  <p class="tx para">Our team plans and runs fast fibre and mobile links for firms across the city. We test each line, watch every node and fix faults before clients notice, so teams stay online and calls stay clear all day long.</p>
</section>

<section class="slide">
  <span class="num">5</span>
  <div class="half">
    <div class="avatar ph" style="margin-top:50px;border-color:var(--navy);box-shadow:none" role="img" aria-label="Portrait photo of the sales director"></div>
    <p class="name" style="color:#fff;font-weight:400;font-size:8px">Owen Marsh</p>
    <p class="sub">Europe and Asia Sales Manager</p>
    <div class="pin"></div>
  </div>
  <p class="tx para" style="position:absolute;top:228px;left:0;right:0">Our team plans and runs fast fibre and mobile links for firms across the city. We test each line, watch every node and fix faults before clients notice, so teams stay online and calls stay clear all day long.</p>
</section>

<section class="slide">
  <span class="num">6</span>
  <h2 class="ttl">Icon List Example</h2>
  <p class="sub">Subtitle Example Here</p>
  <div class="list">
    <div class="item"><span class="dot" style="background:var(--navy)"></span><div><h4>Subtitle Example</h4><p class="tx">Fast links for busy teams. We plan, test and run each line so your calls stay clear.</p></div></div>
    <div class="item"><span class="dot" style="background:var(--blue)"></span><div><h4>Subtitle Example</h4><p class="tx">Fast links for busy teams. We plan, test and run each line so your calls stay clear.</p></div></div>
    <div class="item"><span class="dot" style="background:var(--green)"></span><div><h4>Subtitle Example</h4><p class="tx">Fast links for busy teams. We plan, test and run each line so your calls stay clear.</p></div></div>
    <div class="item"><span class="dot" style="background:var(--lime)"></span><div><h4>Subtitle Example</h4><p class="tx">Fast links for busy teams. We plan, test and run each line so your calls stay clear.</p></div></div>
    <div class="item"><span class="dot" style="background:var(--orange)"></span><div><h4>Subtitle Example</h4><p class="tx">Fast links for busy teams. We plan, test and run each line so your calls stay clear.</p></div></div>
    <div class="item"><span class="dot" style="background:var(--red)"></span><div><h4>Subtitle Example</h4><p class="tx">Fast links for busy teams. We plan, test and run each line so your calls stay clear.</p></div></div>
  </div>
</section>

<section class="slide">
  <span class="num">7</span>
  <h2 class="ttl">Numeric List Example 1</h2>
  <p class="sub">Subtitle Example Here</p>
  <div class="list">
    <div class="item"><span class="n" style="color:var(--navy)">01</span><div><h4>Subtitle Example</h4><p class="tx">Fast links for busy teams. We plan, test and run each line so your calls stay clear.</p></div></div>
    <div class="item"><span class="n" style="color:var(--blue)">02</span><div><h4>Subtitle Example</h4><p class="tx">Fast links for busy teams. We plan, test and run each line so your calls stay clear.</p></div></div>
    <div class="item"><span class="n" style="color:var(--green)">03</span><div><h4>Subtitle Example</h4><p class="tx">Fast links for busy teams. We plan, test and run each line so your calls stay clear.</p></div></div>
    <div class="item"><span class="n" style="color:var(--lime)">04</span><div><h4>Subtitle Example</h4><p class="tx">Fast links for busy teams. We plan, test and run each line so your calls stay clear.</p></div></div>
    <div class="item"><span class="n" style="color:var(--orange)">05</span><div><h4>Subtitle Example</h4><p class="tx">Fast links for busy teams. We plan, test and run each line so your calls stay clear.</p></div></div>
    <div class="item"><span class="n" style="color:var(--red)">06</span><div><h4>Subtitle Example</h4><p class="tx">Fast links for busy teams. We plan, test and run each line so your calls stay clear.</p></div></div>
  </div>
</section>

<section class="slide">
  <span class="num">8</span>
  <h2 class="ttl">Numeric List Example 2</h2>
  <p class="sub">Subtitle Example Here</p>
  <div class="list">
    <div class="item"><span class="nb" style="background:var(--navy)">01</span><div><h4>Subtitle Example</h4><p class="tx">Fast links for busy teams. We plan, test and run each line so your calls stay clear.</p></div></div>
    <div class="item"><span class="nb" style="background:var(--blue)">02</span><div><h4>Subtitle Example</h4><p class="tx">Fast links for busy teams. We plan, test and run each line so your calls stay clear.</p></div></div>
    <div class="item"><span class="nb" style="background:var(--green)">03</span><div><h4>Subtitle Example</h4><p class="tx">Fast links for busy teams. We plan, test and run each line so your calls stay clear.</p></div></div>
    <div class="item"><span class="nb" style="background:var(--lime)">04</span><div><h4>Subtitle Example</h4><p class="tx">Fast links for busy teams. We plan, test and run each line so your calls stay clear.</p></div></div>
    <div class="item"><span class="nb" style="background:var(--orange)">05</span><div><h4>Subtitle Example</h4><p class="tx">Fast links for busy teams. We plan, test and run each line so your calls stay clear.</p></div></div>
    <div class="item"><span class="nb" style="background:var(--red)">06</span><div><h4>Subtitle Example</h4><p class="tx">Fast links for busy teams. We plan, test and run each line so your calls stay clear.</p></div></div>
  </div>
</section>

<section class="slide dark">
  <span class="num">9</span>
  <svg class="stripes" viewBox="0 0 566 318" aria-hidden="true">
    <polygon points="340,318 392,318 592,0 540,0" fill="var(--green)"/>
    <polygon points="398,318 428,318 628,0 598,0" fill="var(--blue)"/>
  </svg>
  <div class="section">
    <div class="sym"></div>
    <h2>Team Section</h2>
    <p class="sub">Subtitle Example</p>
    <p class="tx">Our team plans and runs fast fibre and mobile links for firms across the city. We test each line, watch every node and fix faults before clients notice, so teams stay online and calls stay clear all day long.</p>
  </div>
</section>

<section class="slide">
  <span class="num">10</span>
  <h2 class="ttl" style="padding-top:14px">Worldwide headers</h2>
  <p class="sub">Subtitle Example</p>
  <div class="team" style="grid-template-columns:repeat(3,1fr);gap:20px;padding:10px 36px 0">
    <div class="c"><div class="ph" style="height:140px" role="img" aria-label="Portrait photo of a smiling man"></div><p class="name">Owen Marsh</p><p class="role">CEO Founder</p><p class="tx">A short note on this member and their role.</p><div class="soc"><i></i><i></i><i></i></div></div>
    <div class="c"><div class="ph warm" style="height:140px" role="img" aria-label="Portrait photo of a smiling woman"></div><p class="name">Lena Ortiz</p><p class="role">President</p><p class="tx">A short note on this member and their role.</p><div class="soc"><i></i><i></i><i></i></div></div>
    <div class="c"><div class="ph cool" style="height:140px" role="img" aria-label="Portrait photo of a young man"></div><p class="name">Felix Hale</p><p class="role">General Manager</p><p class="tx">A short note on this member and their role.</p><div class="soc"><i></i><i></i><i></i></div></div>
  </div>
</section>

<section class="slide">
  <span class="num">11</span>
  <h2 class="ttl" style="padding-top:14px">Four team member slide</h2>
  <p class="sub">Subtitle Example</p>
  <div class="team" style="grid-template-columns:repeat(4,1fr);gap:4px;padding:10px 36px 0">
    <div class="c"><div class="ph warm" style="height:140px" role="img" aria-label="Portrait photo of a woman"></div><p class="name">Nora Blake</p><p class="role">General Manager</p><p class="tx">A short note on this member and their role.</p><div class="soc"><i></i><i></i><i></i></div></div>
    <div class="c"><div class="ph" style="height:140px" role="img" aria-label="Portrait photo of a man"></div><p class="name">Adam Kerr</p><p class="role">Account Director</p><p class="tx">A short note on this member and their role.</p><div class="soc"><i></i><i></i><i></i></div></div>
    <div class="c"><div class="ph dusk" style="height:140px" role="img" aria-label="Portrait photo of a woman"></div><p class="name">Iris Fenwick</p><p class="role">Creative Director</p><p class="tx">A short note on this member and their role.</p><div class="soc"><i></i><i></i><i></i></div></div>
    <div class="c"><div class="ph cool" style="height:140px" role="img" aria-label="Portrait photo of a man"></div><p class="name">Theo Grant</p><p class="role">Art Director</p><p class="tx">A short note on this member and their role.</p><div class="soc"><i></i><i></i><i></i></div></div>
  </div>
</section>

<section class="slide dark">
  <span class="num">12</span>
  <h2 class="ttl" style="padding-top:14px">Success profile</h2>
  <p class="sub">Subtitle example</p>
  <div class="success">
    <div class="ph" role="img" aria-label="Photo of a businessman in a grey suit"></div>
    <div class="body">
      <h4>Subtitle Example</h4>
      <p class="tx">Fast links for busy teams. We plan, test and run each line so your calls stay clear.</p>
    </div>
  </div>
  <p class="tx foot">Our team plans and runs fast fibre and mobile links for firms across the city. We test each line, watch every node and fix faults before clients notice, so teams stay online and calls stay clear all day long.</p>
</section>

<section class="slide">
  <span class="num">13</span>
  <h2 class="ttl" style="padding-top:14px">Five team member slide</h2>
  <p class="sub">Subtitle Example</p>
  <div class="team" style="grid-template-columns:repeat(5,1fr);gap:4px;padding:10px 36px 0">
    <div class="c"><div class="ph light" style="height:140px" role="img" aria-label="Portrait photo of a woman"></div><p class="name">Ruby Lane</p><p class="role">General Manager</p><p class="tx">A short note on this member and their role.</p><div class="soc"><i></i><i></i><i></i></div></div>
    <div class="c"><div class="ph warm" style="height:140px" role="img" aria-label="Portrait photo of a woman"></div><p class="name">Maya Cole</p><p class="role">Account Manager</p><p class="tx">A short note on this member and their role.</p><div class="soc"><i></i><i></i><i></i></div></div>
    <div class="c"><div class="ph cool" style="height:140px" role="img" aria-label="Portrait photo of a man"></div><p class="name">Jude Parker</p><p class="role">Creative Director</p><p class="tx">A short note on this member and their role.</p><div class="soc"><i></i><i></i><i></i></div></div>
    <div class="c"><div class="ph light" style="height:140px" role="img" aria-label="Portrait photo of a man"></div><p class="name">Ray Dunn</p><p class="role">Art Director</p><p class="tx">A short note on this member and their role.</p><div class="soc"><i></i><i></i><i></i></div></div>
    <div class="c"><div class="ph dusk" style="height:140px" role="img" aria-label="Portrait photo of a man"></div><p class="name">Omar Reyes</p><p class="role">Sales Director</p><p class="tx">A short note on this member and their role.</p><div class="soc"><i></i><i></i><i></i></div></div>
  </div>
</section>

<section class="slide">
  <span class="num">14</span>
  <h2 class="ttl" style="padding-top:14px">Six team member slide</h2>
  <p class="sub">Subtitle Example</p>
  <div class="six">
    <div class="card"><div class="ph" role="img" aria-label="Portrait photo of a man"></div><div><p class="name" style="margin-top:0">Ethan Cross</p><p class="tx">A short note on this member and their role.</p><div class="soc"><i></i><i></i><i></i></div></div></div>
    <div class="card"><div class="ph warm" role="img" aria-label="Portrait photo of a man"></div><div><p class="name" style="margin-top:0">Hugo Lind</p><p class="tx">A short note on this member and their role.</p><div class="soc"><i></i><i></i><i></i></div></div></div>
    <div class="card"><div class="ph cool" role="img" aria-label="Portrait photo of a man"></div><div><p class="name" style="margin-top:0">Sam Webb</p><p class="tx">A short note on this member and their role.</p><div class="soc"><i></i><i></i><i></i></div></div></div>
    <div class="card"><div class="ph dusk" role="img" aria-label="Portrait photo of a woman"></div><div><p class="name" style="margin-top:0">Ava Morrow</p><p class="tx">A short note on this member and their role.</p><div class="soc"><i></i><i></i><i></i></div></div></div>
    <div class="card"><div class="ph light" role="img" aria-label="Portrait photo of a woman"></div><div><p class="name" style="margin-top:0">Zoe Hart</p><p class="tx">A short note on this member and their role.</p><div class="soc"><i></i><i></i><i></i></div></div></div>
    <div class="card"><div class="ph" role="img" aria-label="Portrait photo of a man"></div><div><p class="name" style="margin-top:0">Leo Ashby</p><p class="tx">A short note on this member and their role.</p><div class="soc"><i></i><i></i><i></i></div></div></div>
  </div>
</section>

<section class="slide dark">
  <span class="num">15</span>
  <svg class="stripes" viewBox="0 0 566 318" aria-hidden="true">
    <polygon points="340,318 392,318 592,0 540,0" fill="var(--green)"/>
    <polygon points="398,318 428,318 628,0 598,0" fill="var(--blue)"/>
  </svg>
  <div class="section">
    <div class="sym"></div>
    <h2>Gallery Section</h2>
    <p class="sub">Subtitle Example Here</p>
    <p class="tx">Our team plans and runs fast fibre and mobile links for firms across the city. We test each line, watch every node and fix faults before clients notice, so teams stay online and calls stay clear all day long.</p>
  </div>
</section>

<section class="slide">
  <span class="num">16</span>
  <div class="tiles">
    <div class="tile" style="background:var(--navy)"><i></i>Short note on this tile.</div>
    <div class="ph" role="img" aria-label="Portrait photo of a man"></div>
    <div class="tile" style="background:var(--blue)"><i></i>Short note on this tile.</div>
    <div class="ph warm" role="img" aria-label="Portrait photo of a woman"></div>
    <div class="tile" style="background:var(--green)"><i></i>Short note on this tile.</div>
    <div class="ph cool" role="img" aria-label="Portrait photo of a man"></div>
    <div class="ph dusk" role="img" aria-label="Portrait photo of a woman"></div>
    <div class="tile" style="background:var(--lime)"><i></i>Short note on this tile.</div>
    <div class="ph" role="img" aria-label="Portrait photo of a man"></div>
    <div class="tile" style="background:var(--orange)"><i></i>Short note on this tile.</div>
    <div class="ph light" role="img" aria-label="Portrait photo of a woman"></div>
    <div class="tile" style="background:var(--red)"><i></i>Short note on this tile.</div>
  </div>
  <p class="name c" style="font-weight:400;font-size:8px;margin-top:18px">Tiles Gallery Example</p>
  <p class="sub">Subtitle Example</p>
  <p class="tx c" style="padding:6px 40px 0">Our team plans and runs fast fibre and mobile links for firms across the city. We test each line, watch every node and fix faults before clients notice, so teams stay online and calls stay clear all day long.</p>
</section>

<section class="slide dark">
  <span class="num">17</span>
  <h2 class="ttl" style="padding-top:14px">Image with text description</h2>
  <p class="sub">Subtitle Example</p>
  <div class="itd">
    <div class="ph cool" role="img" aria-label="Photo of a man working on a laptop in an armchair"></div>
    <div class="panel">
      <h4>Subtitle Example</h4>
      <p class="tx">Fast links for busy teams. We plan, test and run each line so your calls stay clear.</p>
      <div class="circles"><i style="background:var(--blue)"></i><i style="background:var(--green)"></i><i style="background:var(--lime)"></i><i style="background:var(--orange)"></i><i style="background:var(--red)"></i></div>
    </div>
  </div>
  <p class="tx foot">Our team plans and runs fast fibre and mobile links for firms across the city. We test each line, watch every node and fix faults before clients notice, so teams stay online and calls stay clear all day long.</p>
</section>

<section class="slide">
  <span class="num">18</span>
  <h2 class="ttl" style="padding-top:14px">Project Details</h2>
  <p class="sub">Subtitle Example</p>
  <p class="tx intro">Our team plans and runs fast fibre and mobile links for firms across the city. We test each line, watch every node and fix faults before clients notice, so teams stay online and calls stay clear all day long.</p>
  <div class="ph" style="margin:8px 36px 0;height:130px" role="img" aria-label="Photo of commuters walking through a station"></div>
  <p class="name" style="padding:6px 36px 0;font-size:6px;margin:0">Subtitle Example</p>
  <p class="tx" style="padding:2px 36px 0">Our team plans and runs fast fibre and mobile links for firms across the city. We test each line, watch every node and fix faults before clients notice, so teams stay online and calls stay clear all day long.</p>
</section>

<section class="slide">
  <span class="num">19</span>
  <h2 class="ttl" style="padding-top:14px">Gallery with two images</h2>
  <p class="sub">Subtitle Example</p>
  <p class="tx intro">Our team plans and runs fast fibre and mobile links for firms across the city. We test each line, watch every node and fix faults before clients notice, so teams stay online and calls stay clear all day long.</p>
  <div class="gal" style="grid-template-columns:1fr 1fr;gap:12px">
    <div><div class="ph cool" style="height:140px" role="img" aria-label="Photo of hands typing on a laptop"></div><h5>Image title here</h5><p class="tx">A short note on this image and its story.</p></div>
    <div><div class="ph warm" style="height:140px" role="img" aria-label="Photo of a team meeting around a table"></div><h5>Image title here</h5><p class="tx">A short note on this image and its story.</p></div>
  </div>
</section>

<section class="slide">
  <span class="num">20</span>
  <h2 class="ttl" style="padding-top:14px">Gallery with three images</h2>
  <p class="sub">Subtitle Example</p>
  <p class="tx intro">Our team plans and runs fast fibre and mobile links for firms across the city. We test each line, watch every node and fix faults before clients notice, so teams stay online and calls stay clear all day long.</p>
  <div class="gal" style="grid-template-columns:repeat(3,1fr);gap:16px">
    <div><div class="ph" style="height:135px" role="img" aria-label="Photo of a leather notebook and phone"></div><h5>Image title here</h5><p class="tx">A short note on this image and its story.</p></div>
    <div><div class="ph cool" style="height:135px" role="img" aria-label="Photo of a retro digital display"></div><h5>Image title here</h5><p class="tx">A short note on this image and its story.</p></div>
    <div><div class="ph dusk" style="height:135px" role="img" aria-label="Photo of a compass on a desk"></div><h5>Image title here</h5><p class="tx">A short note on this image and its story.</p></div>
  </div>
</section>

<section class="slide dark">
  <span class="num">21</span>
  <h2 class="ttl" style="padding-top:14px">Two images with description</h2>
  <p class="sub">Subtitle Example</p>
  <div class="twin">
    <div class="ph light" role="img" aria-label="Photo of a bright open-plan office"></div>
    <div class="panel">
      <h4>Twice Project</h4>
      <p class="tx">Fast links for busy teams. We plan, test and run each line so your calls stay clear.</p>
      <div class="circles"><i style="background:var(--navy)"></i><i style="background:var(--blue)"></i><i style="background:var(--red)"></i></div>
    </div>
    <div class="ph" role="img" aria-label="Photo of a phone and laptop on a desk"></div>
  </div>
  <p class="tx foot">Our team plans and runs fast fibre and mobile links for firms across the city. We test each line, watch every node and fix faults before clients notice, so teams stay online and calls stay clear all day long.</p>
</section>

<section class="slide">
  <span class="num">22</span>
  <h2 class="ttl" style="padding-top:14px">Gallery with four images</h2>
  <p class="sub">Subtitle Example</p>
  <p class="tx intro">Our team plans and runs fast fibre and mobile links for firms across the city. We test each line, watch every node and fix faults before clients notice, so teams stay online and calls stay clear all day long.</p>
  <div class="gal" style="grid-template-columns:repeat(4,1fr);gap:12px">
    <div><div class="ph cool" style="height:130px" role="img" aria-label="Photo of a modern meeting room"></div><h5>Image title here</h5><p class="tx">A short note on this image and its story.</p></div>
    <div><div class="ph light" style="height:130px" role="img" aria-label="Photo of a person using a tablet"></div><h5>Image title here</h5><p class="tx">A short note on this image and its story.</p></div>
    <div><div class="ph" style="height:130px" role="img" aria-label="Photo of a glass office tower"></div><h5>Image title here</h5><p class="tx">A short note on this image and its story.</p></div>
    <div><div class="ph light" style="height:130px" role="img" aria-label="Photo of a hand writing notes"></div><h5>Image title here</h5><p class="tx">A short note on this image and its story.</p></div>
  </div>
</section>

<section class="slide">
  <span class="num">23</span>
  <h2 class="ttl" style="padding-top:14px">Gallery with five images</h2>
  <p class="sub">Subtitle Example</p>
  <p class="tx intro">Our team plans and runs fast fibre and mobile links for firms across the city. We test each line, watch every node and fix faults before clients notice, so teams stay online and calls stay clear all day long.</p>
  <div class="gal" style="grid-template-columns:repeat(5,1fr);gap:10px">
    <div><div class="ph cool" style="height:130px" role="img" aria-label="Photo of a person on a rooftop"></div><h5>Image title here</h5><p class="tx">A short note on this image and its story.</p></div>
    <div><div class="ph dusk" style="height:130px" role="img" aria-label="Photo of a bright window"></div><h5>Image title here</h5><p class="tx">A short note on this image and its story.</p></div>
    <div><div class="ph warm" style="height:130px" role="img" aria-label="Photo of a figure at sunset"></div><h5>Image title here</h5><p class="tx">A short note on this image and its story.</p></div>
    <div><div class="ph light" style="height:130px" role="img" aria-label="Photo of a road through fields"></div><h5>Image title here</h5><p class="tx">A short note on this image and its story.</p></div>
    <div><div class="ph" style="height:130px" role="img" aria-label="Photo of a desk with devices"></div><h5>Image title here</h5><p class="tx">A short note on this image and its story.</p></div>
  </div>
</section>

<section class="slide">
  <span class="num">24</span>
  <h2 class="ttl" style="padding-top:14px">Gallery with six images</h2>
  <p class="sub">Subtitle Example</p>
  <div class="gal" style="grid-template-columns:repeat(3,1fr);gap:4px 16px;padding-top:14px">
    <div><div class="ph" style="height:62px" role="img" aria-label="Photo of a laptop on a desk"></div><h5>Image title here</h5><p class="tx">A short note on this image and its story.</p></div>
    <div><div class="ph light" style="height:62px" role="img" aria-label="Photo of a hand holding a pen"></div><h5>Image title here</h5><p class="tx">A short note on this image and its story.</p></div>
    <div><div class="ph light" style="height:62px" role="img" aria-label="Photo of a notebook with sketches"></div><h5>Image title here</h5><p class="tx">A short note on this image and its story.</p></div>
    <div><div class="ph cool" style="height:62px" role="img" aria-label="Photo of a lake shore"></div><h5>Image title here</h5><p class="tx">A short note on this image and its story.</p></div>
    <div><div class="ph" style="height:62px" role="img" aria-label="Photo of a camera on a table"></div><h5>Image title here</h5><p class="tx">A short note on this image and its story.</p></div>
    <div><div class="ph light" style="height:62px" role="img" aria-label="Photo of hands typing"></div><h5>Image title here</h5><p class="tx">A short note on this image and its story.</p></div>
  </div>
</section>

<section class="slide dark">
  <span class="num">25</span>
  <h2 class="ttl" style="padding-top:14px">Tile image example</h2>
  <p class="sub">Subtitle Example</p>
  <div class="ti">
    <div class="ph dusk" role="img" aria-label="Photo of colleagues at a laptop"></div>
    <div class="txt" style="background:var(--navy)">
      <h5>Project Detail</h5>
      <p class="tx">Fast links for busy teams. We plan, test and run each line so your calls stay clear.</p>
    </div>
    <div class="ph light" role="img" aria-label="Photo of a person reviewing documents"></div>
    <div class="txt" style="background:var(--green)">
      <h5>Gallery Title</h5>
      <p class="tx" style="color:#f1fbf6">Fast links for busy teams. We plan, test and run each line so your calls stay clear.</p>
    </div>
  </div>
</section>

<section class="slide" style="background:#ececec">
  <div class="tl">
    <div style="background:var(--blue)"><span class="yr">2011</span>Short note on what the team did in this year.</div>
    <div class="ph warm" role="img" aria-label="Photo of a woman in a red top"></div>
    <div class="vert" style="background:var(--blue)"><span>JUNE 2012</span></div>
    <div style="background:var(--blue);grid-column:span 2">Short note on what the team did in this year.</div>
    <div class="ph light" role="img" aria-label="Photo of two people at a laptop"></div>
    <div class="vert" style="background:var(--green)"><span>2013</span></div>
    <div style="background:var(--green)">Short note on what the team did in this year.</div>
    <div style="background:var(--olive);grid-column:span 2"><span class="yr">2014</span>Short note on what the team did in this year.</div>
    <div class="ph" style="grid-column:span 2;grid-row:span 2" role="img" aria-label="Photo of a man using a tablet"></div>
    <div class="vert" style="background:var(--orange)"><span>2015</span></div>
    <div style="background:var(--orange);grid-column:span 3">Short note on what the team did in this year.</div>
    <div class="vert" style="background:var(--red)"><span>MAY 2016</span></div>
    <div style="background:var(--red);grid-column:span 2">Short note on what the team did in this year.</div>
    <div class="vert" style="background:var(--slate)"><span>AUG 2018</span></div>
    <div style="background:var(--slate);grid-column:span 2">Short note on what the team did in this year.</div>
  </div>
</section>

</main>
</body>
</html>
```